New company business cards with new company logo

We need a new business card designed as we have a new company logo and are going for a more 'flat design' look. Our company name is Veridanto and we are a global data focused Clinical Research Organisation. We'd ideally like one side with room for the individuals contact details, our full logo and our services - and one side which is quite plain, for example perhaps using the green triangular image attached with just the white 'V' in the center (also attached).

Industry/Entity Type

Business

Requirements
Must have
• Our main colour: #42b5a9
Please make text dark grey: #373737

```html
<!DOCTYPE html>
<html lang="en">
<head>
<meta charset="utf-8">
<title>Veridanto Business Card</title>
<link rel="stylesheet" href="https://fonts.googleapis.com/css2?family=Open+Sans:wght@400;600&family=Jura:wght@500;600&display=swap">
<style>
  :root {
    --brand-teal: #42b5a9;
    --text-grey: #373737;
    --panel-dark: #3a3a3a;
    --card-white: #ffffff;
    --card-shade: #e4e4e4;
    --stage: #d9dadb;
  }
  * { box-sizing: border-box; margin: 0; padding: 0; }
  html, body {
    width: 1200px; height: 899px; overflow: hidden;
    background: var(--stage);
  }
  .stage { position: relative; width: 1200px; height: 899px; }
  .card {
    position: absolute; left: 250px; width: 700px; height: 400px;
    background: radial-gradient(ellipse at 40% 45%, var(--card-white) 0%, #f4f4f4 55%, var(--card-shade) 100%);
    box-shadow: 0 6px 18px rgba(0,0,0,0.18);
    overflow: hidden;
  }
  .card--back { top: 30px; }
  .card--front { top: 469px; }
  .card__art { position: absolute; inset: 0; }

  .wordmark { position: absolute; display: flex; align-items: center; }
  .wordmark__dot { border-radius: 50%; background: var(--brand-teal); flex: none; }
  .wordmark__text { display: flex; flex-direction: column; }
  .wordmark__name {
    font-family: 'Open Sans', sans-serif; font-weight: 400;
    color: var(--text-grey); line-height: 1.05;
  }
  .wordmark__tagline {
    font-family: 'Open Sans', sans-serif; font-weight: 400; color: var(--text-grey);
    letter-spacing: 0.5px; margin-top: 6px;
  }

  .card--back .wordmark { left: 205px; top: 152px; }
  .card--back .wordmark__dot { width: 92px; height: 92px; margin-right: 16px; }
  .card--back .wordmark__name { font-size: 50px; }
  .card--back .wordmark__tagline { font-size: 17px; }

  .card--front .wordmark { left: 28px; top: 94px; }
  .card--front .wordmark__dot { width: 80px; height: 80px; margin-right: 14px; }
  .card--front .wordmark__name { font-size: 44px; }
  .card--front .wordmark__tagline { font-size: 15px; }

  .person {
    position: absolute; right: 32px; top: 98px; text-align: right;
    color: #fff; font-family: 'Jura', sans-serif;
  }
  .person__name { font-size: 24px; font-weight: 600; letter-spacing: 2px; }
  .person__role { font-size: 18px; font-weight: 600; margin-top: 6px; letter-spacing: 0.5px; }

  .contacts {
    position: absolute; left: 30px; top: 210px; list-style: none;
    font-family: 'Jura', sans-serif; font-weight: 600; color: var(--text-grey);
    font-size: 15px;
  }
  .contacts li { display: flex; align-items: center; height: 27px; }
  .contacts svg { width: 15px; height: 15px; margin-right: 10px; fill: var(--text-grey); flex: none; }
  .contacts .contacts__web, .contacts .contacts__mail { font-size: 13px; }

  .address {
    position: absolute; right: 40px; bottom: 22px;
    font-family: 'Jura', sans-serif; font-weight: 600; font-style: normal; color: var(--text-grey);
    font-size: 17px; line-height: 1.45; letter-spacing: 0.5px;
  }
</style>
</head>
<body>
<main class="stage">

  <section class="card card--back" aria-label="Card back">
    <div class="wordmark">
      <span class="wordmark__dot"></span>
      <div class="wordmark__text">
        <span class="wordmark__name">Veridanto</span>
        <span class="wordmark__tagline">Clinical Data Research</span>
      </div>
    </div>
  </section>

  <section class="card card--front" aria-label="Card front">
    <svg class="card__art" viewBox="0 0 700 400" width="700" height="400" aria-hidden="true">
      <path d="M0 0 H700 V372 C610 150 340 22 0 40 Z" fill="var(--panel-dark)"/>
      <path d="M0 64 C340 28 612 160 700 388 V400 H690 C600 176 340 48 0 74 Z" fill="var(--brand-teal)"/>
    </svg>

    <div class="wordmark">
      <span class="wordmark__dot"></span>
      <div class="wordmark__text">
        <span class="wordmark__name">Veridanto</span>
        <span class="wordmark__tagline">Clinical Data Research</span>
      </div>
    </div>

    <div class="person">
      <p class="person__name">MARK ELLISON</p>
      <p class="person__role">Managing Director</p>
    </div>

    <ul class="contacts">
      <li><svg viewBox="0 0 16 16"><path d="M3 1 L6 1 L7 5 L5 6.5 C6 9 7 10 9.5 11 L11 9 L15 10 L15 13 C15 14 14 15 13 15 C6 15 1 10 1 3 C1 2 2 1 3 1Z"/></svg>012 345 6789</li>
      <li><svg viewBox="0 0 16 16"><path d="M4 0 H12 A1 1 0 0 1 13 1 V15 A1 1 0 0 1 12 16 H4 A1 1 0 0 1 3 15 V1 A1 1 0 0 1 4 0Z M5 2 V12 H11 V2Z M7 13.2 H9 V14.6 H7Z"/></svg>012 345 6789</li>
      <li><svg viewBox="0 0 16 16"><path d="M1 5 H4 V15 H1Z M5 6 H15 V15 H5Z M6 1 H13 V5 H6Z M7 8 H9 V10 H7Z M11 8 H13 V10 H11Z M7 11 H9 V13 H7Z M11 11 H13 V13 H11Z"/></svg>012 345 6789</li>
      <li class="contacts__mail"><svg viewBox="0 0 16 16"><path d="M0 3 H16 V13 H0Z M1.5 4 L8 9 L14.5 4Z" fill-rule="evenodd"/></svg>urname@email.com</li>
      <li class="contacts__web"><svg viewBox="0 0 16 16"><circle cx="8" cy="8" r="7" fill="none" stroke="var(--text-grey)" stroke-width="1.4"/><ellipse cx="8" cy="8" rx="3" ry="7" fill="none" stroke="var(--text-grey)" stroke-width="1.2"/><path d="M1 8 H15" stroke="var(--text-grey)" stroke-width="1.2"/></svg>www.urwebsitename.com</li>
    </ul>

    <address class="address">214.9th floor,Park<br>Harbour Road NTL</address>
  </section>

</main>
</body>
</html>
```